Postcard Mailer for Hospital Audience

We need a postcard mailer designed that will be sent to the financial/business office of a hospital. The postcard will be mailed to hospitals to encourage them to visit our booth at a upcoming trade show.

My company provides solutions that eliminate paper and manual processes for hospital billing offices through the secure electronic exchange of medical documentation.

We would like to see designs that use blues and greens. The final design should communicate financial savings for hospitals by eliminating paper and manual processes through the secure exchange of medical documentation.
Updates

Thank you for the designs and considerations for designs. The postcard does not have to have an image of a hospital or hospital worker, but it must be appealing to a hospital looking to save money.  It will be mailed and must stand-out to make the audience want to look at it and learn more. Eye-catching and a strong impact, is what I am looking for.

Thank you,

Target Market(s)

Hospital Chief Financial Officers, Revenue Cycle Managers, Billing Office Managers, Medical Records Director, HIM Director, Compliance Officer

Industry/Entity Type

Electronic

Requirements
Must have
• Two sided postcard 9"x6" design that includes an area for postage and mailing address.

Text can read: The average hospital can save over ____ per year with Korvit Solutions. Visit us at OPRL KTX Booth #2117 to learn more.

Bring this card for a special gift.
Nice to have
• visit www.korvit-zoom.example to see our corporate colors
Image that illustrates hospitals and/or financial savings.

```html
<!DOCTYPE html>
<html lang="en">
<head>
<meta charset="utf-8">
<title>Korvit Solutions Postcard</title>
<link rel="stylesheet" href="https://fonts.googleapis.com/css2?family=Arimo:wght@400;700&family=Roboto+Condensed:wght@700&display=swap">
<style>
  :root{
    --navy:#0b2a63;
    --navy-text:#12306b;
    --cyan:#2ee0f0;
    --teal:#139aa0;
    --gold:#c9a300;
    --white:#ffffff;
    --stage:#d9d9d9;
    --ink:#333;
  }
  *{box-sizing:border-box;margin:0;padding:0}
  html,body{width:1200px;height:847px;overflow:hidden;background:var(--stage);font-family:"Arimo",Arial,sans-serif}
  .card{position:absolute;top:53px;width:522px;height:742px;overflow:hidden;background:var(--white)}
  .card--front{left:53px}
  .card--back{left:623px}
  .card svg.shapes{position:absolute;inset:0}
  .abs{position:absolute}
  .brand{font-family:"Arimo",Arial,sans-serif;font-weight:700;font-size:24px;color:var(--navy-text);display:flex;align-items:center;gap:7px}
  .brand i{display:inline-block;width:12px;height:12px;background:var(--teal)}
  .intro{left:42px;top:136px;width:170px;font-size:15px;line-height:18px;color:var(--navy-text)}
  .headline{left:45px;top:408px;font-size:28px;line-height:39px;color:var(--white)}
  .headline b{color:var(--cyan)}
  .bullets{left:40px;top:548px;list-style:none;color:var(--white);font-size:16px;line-height:20px}
  .bullets li{position:relative;padding-left:18px;margin-bottom:4px}
  .bullets li::before{content:"";position:absolute;left:0;top:4px;width:10px;height:10px;background:var(--cyan)}
  .badge-text{left:361px;top:560px;width:116px;text-align:center;transform:rotate(-7deg);font-family:"Roboto Condensed",Arial,sans-serif;font-weight:700;color:var(--white);line-height:18px}
  .badge-text .sm{font-size:15px}
  .badge-text .md{font-size:18px}
  .badge-text .lg{font-size:26px;line-height:30px}
  .call{right:20px;top:684px;text-align:right;color:var(--navy-text);font-size:14px}
  .phone-big{right:16px;top:700px;font-family:"Roboto Condensed",Arial,sans-serif;font-weight:700;font-size:28px;color:var(--cyan)}
  .web{left:40px;top:709px;font-weight:700;font-size:16px;color:var(--cyan)}
  .solution h2{font-size:23px;font-weight:400;color:var(--cyan)}
  .solution h2 b{font-weight:700}
  .solution p{margin-top:6px;font-size:12.5px;line-height:19px;color:var(--white)}
  .contact{left:26px;top:420px;list-style:none;color:var(--white);font-weight:700;font-size:13px;line-height:21px}
  .contact li{display:inline-block;position:relative;padding-left:15px;margin-right:20px}
  .contact li::before{content:"";position:absolute;left:0;top:7px;width:7px;height:7px;background:var(--cyan)}
  .contact .row{display:block}
  .return-note{left:20px;top:572px;width:150px;transform-origin:0 0;transform:rotate(90deg) translate(0,-28px);font-size:9.5px;line-height:12px;color:var(--ink)}
  .address-line{position:absolute;top:532px;width:1px;height:173px;background:#777}
  .stamp{position:absolute;left:402px;top:625px;width:86px;height:78px;border:1px solid #555}
</style>
</head>
<body>

<section class="card card--front">
  <svg class="shapes" width="522" height="742" viewBox="0 0 522 742">
    <defs>
      <linearGradient id="photoTone" x1="0" y1="0" x2="1" y2="1">
        <stop offset="0" stop-color="#e9eef3"/><stop offset="1" stop-color="#9fb0c0"/>
      </linearGradient>
      <linearGradient id="deskTone" x1="0" y1="0" x2="1" y2="1">
        <stop offset="0" stop-color="#f2f4f6"/><stop offset="1" stop-color="#a9b7c4"/>
      </linearGradient>
      <radialGradient id="goldTone" cx=".4" cy=".35" r=".7">
        <stop offset="0" stop-color="#f3d23a"/><stop offset="1" stop-color="#a88500"/>
      </radialGradient>
    </defs>
    <rect width="522" height="360" fill="url(#photoTone)" role="img" aria-label="Photo: smiling nurse with stethoscope and clipboard touching a floating Save button"/>
    <path d="M0,0 H265 C220,45 120,72 0,72 Z" fill="var(--white)"/>
    <path d="M0,72 C120,72 220,45 265,0 H300 C250,60 140,105 0,100 Z" fill="var(--cyan)"/>
    <path d="M0,316 C150,372 350,380 522,318 V340 C350,400 150,392 0,336 Z" fill="var(--cyan)"/>
    <path d="M0,336 C150,392 350,400 522,340 V742 H0 Z" fill="var(--navy)"/>
    <path d="M230,742 C320,670 430,640 522,648 V742 Z" fill="var(--teal)"/>
    <path d="M280,742 C360,692 450,672 522,680 V742 Z" fill="var(--white)"/>
    <circle cx="412" cy="357" r="80" fill="url(#deskTone)" stroke="var(--white)" stroke-width="5" role="img" aria-label="Photo: hands holding a card over a laptop keyboard"/>
    <circle cx="419" cy="607" r="58" fill="url(#goldTone)" stroke="var(--white)" stroke-width="3"/>
  </svg>

  <div class="abs brand" style="left:26px;top:28px"><i></i>Korvit</div>
  <p class="abs intro">The healthcare industry. Korvit facilitates electronic requests The healthcare industry. Korvit facilitates electronic requests</p>

  <h1 class="abs headline" style="font-weight:400">The average Hospital<br>can Save over <b>$$$$$</b> per year<br>with <b>Korvit Solutions</b></h1>

  <ul class="abs bullets">
    <li>The healthcare industry. Korvit</li>
    <li>The healthcare industry. Korvit<br>facilitates electronic requests Korvit</li>
    <li>The healthcare industry. Korvit</li>
    <li>The healthcare industry. Korvit</li>
  </ul>

  <div class="abs badge-text">
    <div class="sm">Visit us at</div>
    <div class="md">OPRL KTX</div>
    <div class="sm">Booth</div>
    <div class="lg">2117</div>
  </div>

  <p class="abs call">Call Us Now</p>
  <p class="abs phone-big">555-014-2280</p>
  <p class="abs web">www.korvit-zoom.example</p>
</section>

<section class="card card--back">
  <svg class="shapes" width="522" height="742" viewBox="0 0 522 742">
    <defs>
      <linearGradient id="calcTone" x1="0" y1="0" x2="1" y2="1">
        <stop offset="0" stop-color="#f4f6f8"/><stop offset="1" stop-color="#9eaab6"/>
      </linearGradient>
    </defs>
    <rect width="522" height="412" fill="var(--navy)"/>
    <path d="M275,0 H522 V90 C430,88 330,50 275,0 Z" fill="var(--cyan)"/>
    <path d="M300,0 H522 V80 C440,78 350,45 300,0 Z" fill="var(--white)"/>
    <rect y="412" width="522" height="80" fill="var(--teal)"/>
    <circle cx="130" cy="287" r="100" fill="url(#calcTone)" stroke="var(--white)" stroke-width="5" role="img" aria-label="Photo: hand with pen working on a calculator over paperwork"/>
  </svg>

  <div class="abs brand" style="left:368px;top:24px"><i></i>Korvit</div>

  <div class="abs solution" style="left:47px;top:48px;width:300px">
    <h2><b>Korvit</b> Solutions</h2>
    <p>Korvit offers an electronic medical record request and response solution for the healthcare industry. Korvit facilitates electronic requests for medical records and documentation to connected network providers for payment</p>
  </div>
  <div class="abs solution" style="left:252px;top:173px;width:260px">
    <h2><b>Korvit</b> Solutions</h2>
    <p>Korvit offers an electronic medical record request and response solution for the healthcare industry. Korvit facilitates electronic requests for medical records and documen-</p>
  </div>
  <div class="abs solution" style="left:252px;top:300px;width:260px">
    <h2><b>Korvit</b> Solutions</h2>
    <p>Korvit offers an electronic medical record request and response solution for the healthcare industry. Korvit facilitates electronic</p>
  </div>

  <ul class="abs contact">
    <li class="row">Corporate Office: 410 Alder Court, Suite 12 Fenwick, GA 30000</li>
    <li>Phone : 555-014-2280</li><li>Fax: 555-014-2281</li>
    <li class="row" style="display:block;height:0;padding:0;margin:0"></li>
    <li>E-mail: info@korvit-zoom.example</li><li>Web : www.korvit-zoom.example</li>
  </ul>

  <p class="abs return-note">If undelivered Korvit offers an electronic medical record request and response</p>

  <span class="address-line" style="left:199px"></span>
  <span class="address-line" style="left:244px"></span>
  <span class="address-line" style="left:289px"></span>
  <span class="address-line" style="left:334px"></span>
  <div class="stamp"></div>
</section>

</body>
</html>
```